Startup Consultancy - Brochure Design

This needs to be a digital and potential hardcopy of a glossy brochure, designed to really catch the eye of prospective clients and draw them in. I am looking for something alternative from the "usual", but equally in keeping with the IT industry that the business operate in. The business specifically focuses on Print & Document Software and Technology solutions, and this should be considered in the design.

Target Market(s)

SMB and Corporate End Users, + Technology Resellers

Industry/Entity Type

Information Technology

Other font styles liked:
• Avenir

Colors
9d9d9d
848484
c3c3c3
e8e8e8
ffffff
eaeaea
0255a3
3176b5
85acd3

Requirements
Must have
• Company logo displayed on the front, plus any other relevant placements in pages
• Must follow the colour/style in some way of the website (www.brevantadvisory.co.uk)
Nice to have
• Some kind of infographical style in the brochure would be good, perhaps around the service listings

```html
<!DOCTYPE html>
<html lang="en">
<head>
<meta charset="utf-8">
<title>Brevanta Strategic Consultancy – Brochure</title>
<link href="https://fonts.googleapis.com/css2?family=Open+Sans:wght@300;400;600;700;800&display=swap" rel="stylesheet">
<style>
:root{
  --blue:#0255a3;
  --blue-mid:#3176b5;
  --blue-soft:#85acd3;
  --grey-dark:#333638;
  --grey:#848484;
  --grey-mid:#9d9d9d;
  --grey-light:#c3c3c3;
  --paper:#ffffff;
  --backdrop:#c3c3c3;
  --rule:#e8e8e8;
}
*{box-sizing:border-box;margin:0;padding:0}
html,body{width:1200px;height:2511px;overflow:hidden}
body{background:var(--backdrop);font-family:"Open Sans",Arial,sans-serif;color:var(--grey-dark);position:relative}
.page{position:absolute;width:550px;height:778px;background:var(--paper);overflow:hidden}
.spread{position:absolute;width:1100px;height:778px;box-shadow:0 6px 18px rgba(0,0,0,.18)}
.spread .page-left{left:0;top:0}
.spread .page-right{left:550px;top:0}
.spread .fold{position:absolute;left:540px;top:0;width:20px;height:778px;background:linear-gradient(90deg,rgba(0,0,0,0),rgba(0,0,0,.08),rgba(0,0,0,0));pointer-events:none}
.cover-single{left:325px;top:44px;box-shadow:0 6px 18px rgba(0,0,0,.18)}
.spread-outer{left:50px;top:866px}
.spread-inner{left:50px;top:1688px}

/* brand block */
.brand{position:absolute;left:0;right:0;top:42px;text-align:center}
.brand-name{display:inline-flex;align-items:center;gap:10px;font-size:40px;font-weight:700;color:var(--grey-dark);line-height:1}
.brand-mark{width:26px;height:26px;background:var(--grey-dark)}
.brand-tag{font-size:12px;letter-spacing:3px;color:var(--blue);margin-top:6px;font-weight:600}

/* cover */
.cover-photo{position:absolute;left:160px;top:185px;width:390px;height:315px;background:linear-gradient(135deg,#e9e4dc 0%,#cdb99e 45%,#8a6f52 100%)}
.cover-shape{position:absolute;left:0;top:0}
.cover-headline{position:absolute;left:32px;top:222px;width:230px;color:var(--paper)}
.cover-headline .rule{height:2px;background:var(--paper);width:180px;margin:6px 0}
.cover-headline .w1{font-size:32px;font-weight:800;line-height:1.05}
.cover-headline .w2{font-size:24px;font-weight:300;line-height:1.1}
.cover-headline .w3{font-size:32px;font-weight:300;line-height:1.05}
.cover-headline p{font-size:11.5px;font-weight:700;line-height:1.4;margin-top:12px;width:190px}
.cover-intro{position:absolute;left:110px;top:532px;width:400px;border-left:2px solid var(--grey-dark);padding-left:10px;font-size:12px;line-height:1.5;color:var(--grey)}
.cover-footer{position:absolute;left:60px;right:40px;top:708px;border-top:2px solid var(--grey-dark);padding-top:10px;font-size:19px;font-weight:400;color:var(--grey-dark)}
.cover-footer b{font-weight:700}

/* back page */
.back{padding:30px 34px}
.h-about{font-size:24px;color:var(--blue);font-weight:600;border-bottom:1px solid var(--grey-light);padding-bottom:2px}
.sub{font-size:12px;color:var(--grey);font-weight:600;margin:3px 0 6px}
.body-s{font-size:8.5px;line-height:1.5;color:var(--grey);margin-bottom:6px}
.back-photo{position:absolute;left:0;top:268px;width:550px;height:272px;background:radial-gradient(circle at 45% 45%,#c8b21c 0%,#5f6b10 22%,#1d2410 48%,#050505 80%)}
.back-lower{position:absolute;left:34px;right:34px;top:556px}
.back-lower strong{font-size:10px;color:var(--grey-dark);display:block;margin-bottom:3px}
.socials{position:absolute;right:34px;top:632px;display:flex;gap:6px}
.socials i{width:18px;height:18px;border-radius:50%;background:var(--blue-mid);display:block}
.contact{position:absolute;left:34px;top:660px;width:320px}
.contact h3{font-size:20px;color:var(--blue);font-weight:600;border-bottom:1px solid var(--grey-light);margin-bottom:4px}
.contact ul{list-style:none}
.contact li{display:flex;align-items:center;gap:6px;font-size:10.5px;color:var(--grey-dark);line-height:1.55}
.contact li .dot{width:10px;height:10px;border-radius:50%;background:var(--grey-dark);flex:none}
.contact li.web{font-weight:700;font-size:11.5px}

/* inside pages */
.inner{padding:28px 34px}
.h-sec{font-size:20px;font-weight:700;color:var(--grey-dark);border-bottom:1.5px solid var(--grey-dark);padding-bottom:1px}
.h-sec em{font-style:normal;color:var(--blue)}
.h-small{font-size:13px;font-weight:700;color:var(--grey-dark);margin-top:6px}
.h-small em{font-style:normal;color:var(--blue)}
.h-caps{font-size:18px;font-weight:700;color:var(--blue);border-bottom:1.5px solid var(--grey-dark);margin-top:8px}
.ticks{list-style:none;margin-top:4px}
.ticks li{font-size:8.5px;color:var(--grey);line-height:1.6;padding-left:14px;position:relative}
.ticks li::before{content:"";position:absolute;left:2px;top:2px;width:4px;height:7px;border:solid var(--blue);border-width:0 1.5px 1.5px 0;transform:rotate(45deg)}
.inner-footer{position:absolute;left:0;bottom:0;width:550px;height:70px}
.inner-url{position:absolute;font-size:9px;font-weight:700;color:var(--grey-dark)}
.svc-title{font-size:15px;font-weight:700;color:var(--blue);border-bottom:1.5px solid var(--grey-dark);margin-top:10px}
.svc-title:first-child{margin-top:0}
.svc-sub{font-size:12px;color:var(--grey-dark);margin:2px 0 4px}
.steps{list-style:none}
.steps li{display:flex;gap:8px;font-size:8.5px;line-height:1.45;color:var(--grey);margin-bottom:4px}
.steps li b{color:var(--grey-dark)}
.num{flex:none;width:16px;height:16px;border-radius:50%;background:var(--blue);color:var(--paper);font-size:9px;font-weight:700;display:flex;align-items:center;justify-content:center}
</style>
</head>
<body>

<!-- Front cover -->
<section class="page cover-single">
  <svg class="cover-shape" width="550" height="778" viewBox="0 0 550 778" aria-hidden="true">
    <path d="M550 440 L505 485 L550 530 Z" fill="var(--blue)"/>
  </svg>
  <div class="brand"><div class="brand-name"><span class="brand-mark"></span>Brevanta</div><div class="brand-tag">STRATEGIC CONSULTANCY</div></div>
  <div class="cover-photo" role="img" aria-label="Photograph of a consultant working at a laptop on a desk with notes and a plant"></div>
  <svg class="cover-shape" width="550" height="778" viewBox="0 0 550 778" aria-hidden="true">
    <path d="M0 140 L150 140 Q165 140 175 150 L320 295 Q332 307 320 320 L175 465 Q165 475 150 475 L0 475 Z" fill="var(--blue)"/>
  </svg>
  <div class="cover-headline">
    <div class="rule"></div>
    <div class="w1">WELCOME</div><div class="w2">TO A NEW</div><div class="w3">APPROACH</div>
    <div class="rule"></div>
    <p>We have a range of services suitable for a range of clients including End Users, Channel Partners, OEM's and Distributors.</p>
  </div>
  <p class="cover-intro">Lorem ipsum dolor sit amet, consectetur adipiscing elit. Cras turpis erat, condimentum non eros vitae, sollicitudin tristique arcu. Nam faucibus, urna et malesuada dapibus, leo nulla porta lectus, ut egestas diam magna vitae nunc.</p>
  <div class="cover-footer">www.<b>brevantadvisory</b>.co.uk</div>
</section>

<!-- Outer spread: back + front -->
<section class="spread spread-outer">
  <div class="page page-left back">
    <h2 class="h-about">About Us</h2>
    <p class="sub">Taking a different path</p>
    <p class="body-s">We provide services to End User organisations of various sizes, shapes and styles ranging from SMB through to Enterprise and Government, across a range of vertical markets, helping them create a forward-looking strategy for print and document workflow.</p>
    <p class="body-s">Our expertise, experience and services also support Channel Partners, OEM's and Distributors, providing guidance and advice on print and document workflow strategies, promoting a customer-led focus and building long-term value in every engagement.</p>
    <p class="body-s">As a group of very experienced, highly skilled and committed members of the print and document solutions industry, we grew tired of the lack of true, unbiased and trusted advice within the industry that both Channel Partners and End Users would value.</p>
    <div class="back-photo" role="img" aria-label="Dark photograph with soft yellow and green out-of-focus light circles"></div>
    <div class="back-lower">
      <strong>We don't sell hardware. We don't even sell software.</strong>
      <p class="body-s">We remain independent of any manufacturers and are not affiliated to any partner or dealer. What we do provide however is trusted, valuable consultancy, design and advice. We have no bias.</p>
    </div>
    <div class="socials"><i></i><i></i></div>
    <div class="contact">
      <h3>Contact Us</h3>
      <ul>
        <li><span class="dot"></span>14 Harlow Lane, London, EC1V 4PQ</li>
        <li><span class="dot"></span>0203 555 0182</li>
        <li><span class="dot"></span>enquiries@brevantadvisory.co.uk</li>
        <li class="web">www.brevantadvisory.co.uk</li>
      </ul>
    </div>
  </div>
  <div class="page page-right">
    <svg class="cover-shape" width="550" height="778" viewBox="0 0 550 778" aria-hidden="true">
      <path d="M550 440 L505 485 L550 530 Z" fill="var(--blue)"/>
    </svg>
    <div class="brand"><div class="brand-name"><span class="brand-mark"></span>Brevanta</div><div class="brand-tag">STRATEGIC CONSULTANCY</div></div>
    <div class="cover-photo" role="img" aria-label="Photograph of a consultant working at a laptop on a desk with notes and a plant"></div>
    <svg class="cover-shape" width="550" height="778" viewBox="0 0 550 778" aria-hidden="true">
      <path d="M0 140 L150 140 Q165 140 175 150 L320 295 Q332 307 320 320 L175 465 Q165 475 150 475 L0 475 Z" fill="var(--blue)"/>
    </svg>
    <div class="cover-headline">
      <div class="rule"></div>
      <div class="w1">WELCOME</div><div class="w2">TO A NEW</div><div class="w3">APPROACH</div>
      <div class="rule"></div>
      <p>We have a range of services suitable for a range of clients including End Users, Channel Partners, OEM's and Distributors.</p>
    </div>
    <p class="cover-intro">Lorem ipsum dolor sit amet, consectetur adipiscing elit. Cras turpis erat, condimentum non eros vitae, sollicitudin tristique arcu. Nam faucibus, urna et malesuada dapibus, leo nulla porta lectus, ut egestas diam magna vitae nunc.</p>
    <div class="cover-footer">www.<b>brevantadvisory</b>.co.uk</div>
  </div>
  <div class="fold"></div>
</section>

<!-- Inner spread -->
<section class="spread spread-inner">
  <div class="page page-left inner">
    <h2 class="h-sec">Why Choose <em>Us?</em></h2>
    <p class="sub">An alternative and innovative approach</p>
    <p class="body-s">We take pride, satisfaction and enjoyment from providing clients with clear, non-biased advice. Our determination to stand alone in the industry, without commercial affiliations, lets us deliver an honest view of every print and document environment we review.</p>
    <p class="body-s">We consistently monitor the marketplace and keep up to date with the latest developments in hardware, software and services, so the strategies we design remain relevant and lasting.</p>
    <h3 class="h-sec" style="margin-top:8px">How do we <em>do that?</em></h3>
    <p class="body-s" style="margin-top:6px">Honest and expert advice, transparency in our approach and the integrity to ensure we always put our clients first. We work alongside your team to understand your goals and shape a plan.</p>
    <p class="body-s">Our consultancy services are tailored to each client so that every recommendation is practical, measurable and aligned with the wider business strategy.</p>
    <h4 class="h-small">Services for <em>Channel Partners, OEM's or Distributors</em></h4>
    <p class="body-s">Lorem ipsum dolor sit amet, consectetur adipiscing elit, sed do eiusmod tempor incididunt ut labore et dolore.</p>
    <h4 class="h-small">Services for <em>End User Organisations</em></h4>
    <p class="body-s">Lorem ipsum dolor sit amet, consectetur adipiscing elit, sed do eiusmod tempor incididunt ut labore.</p>
    <h4 class="h-small">How do Brevanta engage on a project, <em>large or small?</em></h4>
    <p class="body-s">Lorem ipsum dolor sit amet, consectetur adipiscing elit. Cras turpis erat, condimentum non eros vitae.</p>
    <h3 class="h-caps">TRAINING SERVICES</h3>
    <ul class="ticks">
      <li>Creation and agreement of training objectives including content specifics</li>
      <li>Skills summary of staff, including separation of training groups</li>
      <li>Training template and plan provided</li>
    </ul>
    <svg class="inner-footer" width="550" height="70" viewBox="0 0 550 70" aria-hidden="true">
      <path d="M0 40 L550 70 L0 70 Z" fill="var(--blue)"/>
    </svg>
    <div class="inner-url" style="left:34px;bottom:44px">www.brevantadvisory.co.uk</div>
  </div>
  <div class="page page-right inner">
    <h3 class="svc-title">STRATEGY DESIGN SERVICES</h3>
    <p class="svc-sub">A roadmap for your future</p>
    <ol class="steps">
      <li><span class="num">1</span><span><b>Stakeholder Interviews &amp; Feedback</b> – a key element right at the beginning of the process, helping us understand your organisation in detail.</span></li>
      <li><span class="num">2</span><span><b>Objective &amp; Goal Mapping</b> – where does your organisation need to get to, and what are the key priorities?</span></li>
      <li><span class="num">3</span><span><b>Departmental/Process Review</b> – what is done where in the current organisation structure.</span></li>
      <li><span class="num">4</span><span><b>Gap Analysis</b> – understanding the gaps and areas to address between the current state and the desired future.</span></li>
      <li><span class="num">5</span><span><b>Strategic Design Proposal</b> – based on all findings, the new strategic design proposal is presented.</span></li>
      <li><span class="num">6</span><span><b>Final Design &amp; Project Plan</b> – the final design is agreed and signed off by all key stakeholders.</span></li>
    </ol>
    <h3 class="svc-title">OPERATIONAL DESIGN SERVICES</h3>
    <p class="svc-sub">A crucial success factor</p>
    <ol class="steps">
      <li><span class="num">1</span><span><b>Stakeholder Interviews &amp; Feedback</b> – a key element right at the beginning of the process, capturing operational detail.</span></li>
      <li><span class="num">2</span><span><b>Objective &amp; Goal Mapping</b> – where does your organisation need to get to with new operational plans?</span></li>
      <li><span class="num">3</span><span><b>Departmental/Process Review</b> – the current workflows, who and how.</span></li>
      <li><span class="num">4</span><span><b>Gap Analysis</b> – understanding the gaps and areas to address between current and future state.</span></li>
      <li><span class="num">5</span><span><b>Final Design &amp; Project Plan</b> – the final operational design and roll-out plan are agreed.</span></li>
    </ol>
    <h3 class="svc-title">TENDER CONSULTANCY &amp; WRITING SERVICES</h3>
    <p class="body-s" style="margin-top:4px">End User tenders are a complex process. We help you define requirements, write the specification and evaluate responses fairly.</p>
    <svg class="inner-footer" width="550" height="70" viewBox="0 0 550 70" aria-hidden="true">
      <path d="M0 70 L550 30 L550 70 Z" fill="var(--blue)"/>
    </svg>
    <div class="inner-url" style="right:34px;bottom:50px">www.brevantadvisory.co.uk</div>
  </div>
  <div class="fold"></div>
</section>

</body>
</html>
```